GPS SALES

Lopoking to design a website for my company " Marbury Designs"
Our slogan is "GPS that's shaped to suit"

I sell in dash gps systems for cars that are built into the dash board. No gaps after install. designed specifically for specific cars.
I have products for all manufacturers...

Want lots of colour!
Online ordering system with payment options online

This is a sales only website....

A site that sells similar products is:
http://e.vantelmo.cn/
I want my website to be very similar to this one.

Im basically selling these products here in australia. So I really want something "australian themed" (kangaroo or koala or australia map....)this kind of thing

Looking to attract business from car dealerships and the public.

I have attached a copy of my brochure, and some of the products I sell

```html
<!DOCTYPE html>
<html lang="en">
<head>
<meta charset="utf-8">
<title>Marbury Designs – GPS that's shaped to suit</title>
<link href="https://fonts.googleapis.com/css2?family=Lato:ital,wght@0,400;0,700;0,900;1,400&family=Open+Sans:wght@400;600&display=swap" rel="stylesheet">
<style>
:root{
  --blue:#0a70c4;
  --blue-dark:#1f4fa3;
  --blue-light:#1a9be0;
  --orange:#f58220;
  --orange-light:#fba93a;
  --ink:#222;
  --text:#333;
  --grey:#888;
  --line:#d8d8d8;
  --white:#fff;
}
*{margin:0;padding:0;box-sizing:border-box}
html,body{width:1128px;height:1200px;overflow:hidden;background:var(--white)}
body{position:relative;font-family:"Lato",sans-serif;color:var(--text)}
.abs{position:absolute}

.topbar{left:0;top:0;width:1128px;height:31px;background:var(--blue);color:var(--white)}
.topbar .tagline{left:130px;top:9px;font-size:11.5px;font-style:italic}
.topbar .contact{top:7px;font-size:14px;display:flex;align-items:center;gap:6px;font-family:"Open Sans",sans-serif;white-space:nowrap}
.topbar svg{fill:var(--white)}

.brand{left:134px;top:58px;display:flex;align-items:center;gap:12px}
.brand .mark{width:42px;height:42px;border-radius:50%;background:var(--orange)}
.brand .name{font-size:34px;font-weight:900;color:var(--blue)}

.social{top:52px;width:36px;height:36px;border-radius:50%;box-shadow:0 2px 3px rgba(0,0,0,.3)}
.social.one{left:877px;background:var(--blue-light)}
.social.two{left:921px;background:#eee}
.social.three{left:964px;background:#eee}

.nav{top:101px;left:481px;display:flex;font-family:"Open Sans",sans-serif;font-size:13px;font-weight:600;color:var(--ink)}
.nav a{display:block;height:25px;line-height:25px;color:inherit;text-decoration:none;margin-right:31px}
.nav a:last-child{margin-right:0}
.nav a.active{background:var(--orange);color:var(--white);padding:0 19px;margin-right:12px}

.hero{left:0;top:149px;width:1128px;height:482px;background:linear-gradient(180deg,#8e8f91 0%,#5e6063 45%,#77797c 100%)}
.arrow{top:333px;width:36px;height:36px;border-radius:50%;background:var(--white);box-shadow:0 2px 4px rgba(0,0,0,.4);display:flex;align-items:center;justify-content:center}
.caption{left:126px;top:528px;width:878px;height:103px;background:rgba(235,235,235,.72);border-radius:4px 4px 0 0}
.caption h1{position:absolute;top:12px;width:100%;text-align:center;font-size:35px;font-weight:700;color:#111}
.dots{left:443px;top:597px;width:243px;height:54px;background:linear-gradient(#fafafa,#e4e4e4);border-radius:4px;box-shadow:0 3px 6px rgba(0,0,0,.25);display:flex;justify-content:center;gap:12px;padding-top:19px}
.dots span{width:13px;height:13px;border-radius:50%;background:var(--orange)}
.dots span.on{background:var(--blue-light);width:15px;height:15px;margin-top:1px}
.hero-shadow{left:160px;top:632px;width:760px;height:22px;border-radius:50%;background:radial-gradient(ellipse at center top,rgba(0,0,0,.18),transparent 70%)}

.panel{top:714px;background:var(--white);border:1px solid #e6e6e6;box-shadow:0 0 3px rgba(0,0,0,.08)}
.panel h2{position:absolute;top:10px;font-size:22px;font-weight:400;color:var(--ink)}
.panel .rule{position:absolute;top:41px;height:1px;background:var(--blue)}
.about{left:125px;width:594px;height:270px}
.about h2{left:12px}
.about .rule{left:12px;width:578px}
.about .photo{left:13px;top:52px;width:243px;height:104px;border:4px solid #eee;background:linear-gradient(135deg,#2a2d33,#0d0f12 60%,#3a3f48)}
.about p{position:absolute;left:12px;top:49px;width:571px;font-size:12.8px;line-height:18.2px;text-align:justify;letter-spacing:.25px}
.about p .float{float:left;width:253px;height:108px}
.btn{left:11px;top:225px;height:24px;padding:0 10px;line-height:24px;background:var(--orange);color:var(--white);font-size:12px;font-weight:700}

.news{left:739px;width:264px;height:267px}
.news h2{left:10px}
.news .rule{left:10px;width:242px}
.news .pager{top:13px;width:18px;height:18px;border:1.5px solid #888;border-radius:50%;display:flex;align-items:center;justify-content:center}
.item{left:10px;width:242px;height:74px}
.item + .item{border-top:1px dotted #aaa}
.date{position:absolute;left:4px;width:35px}
.date .day{height:22px;background:var(--orange);color:var(--white);font-weight:700;font-size:16px;text-align:center;line-height:22px}
.date .mon{height:15px;background:var(--blue);color:var(--white);font-size:11px;text-align:center;line-height:15px}
.item h3{position:absolute;left:59px;font-size:12.5px;font-weight:700;color:var(--ink)}
.item p{position:absolute;left:59px;width:180px;font-size:12.5px;line-height:15px;color:var(--text)}

.footer{left:0;top:1010px;width:1128px;height:190px;background:linear-gradient(180deg,#1493dc 0%,var(--blue-dark) 100%);color:var(--white)}
.signup{left:434px;top:47px;display:flex;align-items:center;gap:12px}
.signup .field{width:183px;height:28px;background:var(--white);color:#999;font-size:12.5px;line-height:28px;padding-left:5px}
.signup .go{width:36px;height:28px;background:var(--orange);font-weight:700;font-size:14px;line-height:28px;text-align:center;margin-left:-12px}
.fnav{top:87px;left:0;width:1128px;display:flex;justify-content:center;gap:52px;font-family:"Open Sans",sans-serif;font-size:12.5px}
.fnav a{color:inherit;text-decoration:none}
.frule{left:138px;top:115px;width:850px;height:1px;background:rgba(255,255,255,.3)}
.finfo{top:125px;font-size:12.5px;display:flex;gap:6px;line-height:15px;white-space:nowrap}
.finfo svg{fill:var(--white);flex:none}
.copy{top:165px;width:100%;text-align:center;font-size:11.5px}
</style>
</head>
<body>

<div class="topbar abs">
  <div class="tagline abs">Lorem ipsum dolor sit amet, consectetur adipiscing elit, sed do eiusmod tempor incididunt ut labore.</div>
  <div class="contact abs" style="left:706px">
    <svg width="9" height="16" viewBox="0 0 9 16"><path d="M2 0h3l1 4-2 1c0 2 1 5 2 6l2-1 1 4-2 2C3 15 0 9 0 4z"/></svg>0412 555 018
  </div>
  <div class="contact abs" style="left:830px">
    <svg width="18" height="13" viewBox="0 0 18 13"><path d="M0 0h18v13H0zM2 2v1l7 5 7-5V2L9 7z" fill-rule="evenodd"/></svg>sales@marbury.com.au
  </div>
</div>

<div class="brand abs"><span class="mark"></span><span class="name">Marbury Designs</span></div>

<span class="social one abs"></span>
<span class="social two abs"></span>
<span class="social three abs"></span>

<nav class="nav abs">
  <a class="active" href="#">HOME</a>
  <a href="#">PRODUCTS</a>
  <a href="#">SERVICES</a>
  <a href="#">ABOUT US</a>
  <a href="#">NEWS</a>
  <a href="#">CONTACT US</a>
</nav>

<div class="hero abs" role="img" aria-label="Photo of a car dashboard with a built-in GPS media screen"></div>
<div class="arrow abs" style="left:86px"><svg width="12" height="14" viewBox="0 0 12 14"><path d="M9 1L3 7l6 6" stroke="#222" stroke-width="3" fill="none"/></svg></div>
<div class="arrow abs" style="left:1006px"><svg width="12" height="14" viewBox="0 0 12 14"><path d="M3 1l6 6-6 6" stroke="#222" stroke-width="3" fill="none"/></svg></div>
<div class="caption abs"><h1>GPS that's shaped to suit</h1></div>
<div class="hero-shadow abs"></div>
<div class="dots abs"><span></span><span></span><span></span><span></span><span class="on"></span></div>

<section class="panel about abs">
  <h2>ABOUT US</h2>
  <div class="rule"></div>
  <p><span class="float"></span>Lorem ipsum dolor sit amet, consectetur adipiscing elit, sed do eiusmod tempor incididunt ut labore et dolfdsigi ore magna aliqua. Ut enim ad minim veniam, qsdgvyiuis nostrud exercitation ullamco laboris nisi ut aliqasdgiuip exesdfgsdfa commodo consequat. Duis aute irure doilor in reprehe nderit in voluptate velit tyed ut perspiciatis unde omnis iste natus error sit voluptatem accusantium doloremque laudasdiantium, totam rem aperiam, eaque ipsa quae ab illo inventore veritatis et quasi architecto beatae vitae dicta sunt explicabo. Nemo enim ipsam voluptatem quia Sed ut perspiciatis.</p>
  <div class="photo abs" role="img" aria-label="Photo of an in-dash GPS unit showing its app menu"></div>
  <div class="btn abs">READ MORE</div>
</section>

<section class="panel news abs">
  <h2>LATEST NEWS</h2>
  <span class="pager abs" style="left:213px"><svg width="10" height="8" viewBox="0 0 10 8"><path d="M9 4H2M4 1L1 4l3 3" stroke="#888" fill="none"/></svg></span>
  <span class="pager abs" style="left:236px;border-color:#333"><svg width="10" height="8" viewBox="0 0 10 8"><path d="M1 4h7M6 1l3 3-3 3" stroke="#333" fill="none"/></svg></span>
  <div class="rule"></div>
  <div class="item abs" style="top:52px"><div class="date" style="top:7px"><div class="day">11</div><div class="mon">NOV</div></div><h3 style="top:5px">Lorem Ipsum Dolor Sit</h3><p style="top:20px">Lorem ipsum dolor sit ametcnhj onsectetuer adimpiscig.</p></div>
  <div class="item abs" style="top:126px"><div class="date" style="top:5px"><div class="day">10</div><div class="mon">NOV</div></div><h3 style="top:3px">Lorem Ipsum Dolor Sit</h3><p style="top:18px">Lorem ipsum dolor sit ametcnhj onsectetuer adimpiscig.</p></div>
  <div class="item abs" style="top:200px"><div class="date" style="top:6px"><div class="day">08</div><div class="mon">NOV</div></div><h3 style="top:4px">Lorem Ipsum Dolor Sit</h3><p style="top:19px">Lorem ipsum dolor sit ametcnhj onsectetuer adimpiscig.</p></div>
</section>

<svg class="abs" style="left:0;top:1008px" width="1128" height="34" viewBox="0 0 1128 34" preserveAspectRatio="none">
  <path d="M0 0L564 22L1128 0V34H0z" fill="var(--orange-light)"/>
</svg>

<footer class="footer abs">
  <svg class="abs" style="left:0;top:0" width="1128" height="12" viewBox="0 0 1128 12" preserveAspectRatio="none"><path d="M0 12L564 0 1128 12V0H0z" fill="var(--orange-light)"/></svg>
  <div class="signup abs">
    <svg width="28" height="26" viewBox="0 0 28 26"><path d="M1 10L14 1l13 9v15H1z" fill="#fff"/><circle cx="14" cy="11" r="4" fill="none" stroke="#1a8ad4" stroke-width="1.5"/><path d="M1 25l10-9M27 25L17 16" stroke="#1a8ad4"/></svg>
    <div class="field">Enter your E-mail here</div>
    <div class="go">GO</div>
  </div>
  <nav class="fnav abs">
    <a href="#">HOME</a><a href="#">PRODUCTS</a><a href="#">SERVICES</a><a href="#">ABOUT US</a><a href="#">NEWS</a><a href="#">CONTACT US</a>
  </nav>
  <div class="frule abs"></div>
  <div class="finfo abs" style="left:242px"><svg width="10" height="14" viewBox="0 0 10 14"><path d="M5 0a5 5 0 0 1 5 5c0 4-5 9-5 9S0 9 0 5a5 5 0 0 1 5-5zm0 3a2 2 0 1 0 0 4 2 2 0 0 0 0-4z" fill-rule="evenodd"/></svg><span>Contrary to popular belief,<br>Lorem Ipsum is.</span></div>
  <div class="finfo abs" style="left:443px"><svg width="12" height="14" viewBox="0 0 9 16"><path d="M2 0h3l1 4-2 1c0 2 1 5 2 6l2-1 1 4-2 2C3 15 0 9 0 4z"/></svg><span>0412 555 018</span></div>
  <div class="finfo abs" style="left:584px"><svg width="18" height="13" viewBox="0 0 18 13"><path d="M0 0h18v13H0zM2 2v1l7 5 7-5V2L9 7z" fill-rule="evenodd"/></svg><span>sales@marbury.com.au</span></div>
  <div class="finfo abs" style="left:768px"><svg width="17" height="14" viewBox="0 0 17 14"><path d="M4 0h9v4H4zM0 5h17v6h-3v3H3v-3H0zm5 3v4h7V8z" fill-rule="evenodd"/></svg><span>02 5550 1234</span></div>
  <div class="copy abs">© 2014. <b>Marbury Designs</b>. All Rights Reserved.</div>
</footer>

</body>
</html>
```